Morrow Poolworks, LLC Business Card

We have a well designed logo that we need incorporated into a professional and unique business card. Morrow Poolworks provides professional swimming pool management. From openings to closings, inspections, chemicals, maintenance, lifeguard, safety audits, learn to swim lessons, etc. etc.
Different colors of blue are ideal. The final design should include water, clean water (very clean crystal clear water), and perhaps safety.
content/design ideas:
Felix Brant, President - Owner
felix@morrowpoolworks.example
office: 555-410-3826
cell: 555-962-1507
www.morrowpoolworks.example
"Clean Water. Safe Swims. Every Day."
Target Market(s)
Our customers are mostly home owners associations and property management companies. Adults, aged 25 to 55. Mostly with young children.
Industry/Entity Type
Safety
Look and feel

```html
<!DOCTYPE html>
<html lang="en">
<head>
<meta charset="utf-8">
<title>Morrow Poolworks, LLC – Business Card</title>
<link rel="stylesheet" href="https://fonts.googleapis.com/css2?family=Arimo&family=Jost:wght@400;600;700&display=swap">
<style>
  :root {
    --board: #808080;
    --label: #ffffff;
    --water-deep: #0a4fa8;
    --water-mid: #1366c4;
    --water-light: #2a86dc;
    --paper: #ffffff;
    --ink: #f2f6fb;
    --brand-blue: #2a6fb8;
  }
  * { margin: 0; padding: 0; box-sizing: border-box; }
  html, body { width: 1200px; height: 1000px; overflow: hidden; }
  body {
    background: var(--board);
    font-family: "Jost", "Futura", sans-serif;
    position: relative;
  }
  .side-label {
    position: absolute;
    left: 82px;
    font-family: "Arimo", Arial, sans-serif;
    font-size: 38px;
    font-weight: 400;
    line-height: 1;
    color: var(--label);
  }
  .side-label--front { top: 284px; }
  .side-label--back { top: 727px; }

  .card {
    position: absolute;
    left: 250px;
    width: 704px;
    height: 414px;
    overflow: hidden;
  }
  .card--front { top: 95px; }
  .card--back { top: 538px; }

  .card__water {
    position: absolute; inset: 0;
    background:
      radial-gradient(ellipse at 30% 40%, var(--water-light) 0%, transparent 60%),
      radial-gradient(ellipse at 75% 85%, var(--water-light) 0%, transparent 55%),
      linear-gradient(160deg, var(--water-mid), var(--water-deep));
  }
  .card__shape { position: absolute; inset: 0; }

  .holder__name {
    position: absolute; left: 48px; top: 38px;
    font-size: 46px; font-weight: 700; letter-spacing: 1px;
    line-height: 1.2; color: var(--ink);
  }
  .holder__title {
    position: absolute; left: 49px; top: 95px;
    font-size: 31px; font-weight: 700; letter-spacing: 0.6px;
    line-height: 1.2; color: var(--ink);
  }
  .contact {
    position: absolute; left: 49px; top: 226px;
    list-style: none;
    font-size: 21px; font-weight: 700; letter-spacing: 0.3px;
    color: var(--ink);
  }
  .contact li { height: 40.5px; }

  .brand {
    position: absolute;
    color: var(--brand-blue);
    font-weight: 600;
    line-height: 1.05;
    display: flex; align-items: center; gap: 10px;
  }
  .brand__dot {
    width: 16px; height: 16px; border-radius: 50%;
    background: var(--brand-blue); flex: none;
  }
  .brand--front { left: 470px; top: 138px; font-size: 38px; }
  .brand--back { left: 170px; top: 160px; font-size: 44px; }

  .tagline {
    position: absolute; left: 0; right: 0; top: 284px;
    text-align: center;
    font-size: 27px; font-weight: 700; letter-spacing: 0.3px;
    color: var(--ink);
  }
</style>
</head>
<body>
  <span class="side-label side-label--front">front</span>
  <span class="side-label side-label--back">back</span>

  <section class="card card--front">
    <div class="card__water" role="img" aria-label="Clear blue pool water with light ripples"></div>
    <svg class="card__shape" viewBox="0 0 704 414" aria-hidden="true">
      <path d="M478 0 H704 V405 C630 375 575 320 535 265 C505 225 455 215 400 225 Z" fill="var(--paper)"/>
    </svg>
    <h1 class="holder__name">Felix Brant</h1>
    <p class="holder__title">President - Owner</p>
    <ul class="contact">
      <li>Office: 555-410-3826</li>
      <li>Cell: 555-962-1507</li>
      <li>felix@morrowpoolworks.example</li>
      <li>www.morrowpoolworks.example</li>
    </ul>
    <div class="brand brand--front">
      <span class="brand__dot"></span>
      <span>Morrow<br>Poolworks</span>
    </div>
  </section>

  <section class="card card--back">
    <div class="card__water" role="img" aria-label="Clear blue pool water with light ripples"></div>
    <svg class="card__shape" viewBox="0 0 704 414" aria-hidden="true">
      <path d="M208 0 H704 V218 H120 Z" fill="var(--paper)"/>
    </svg>
    <div class="brand brand--back">
      <span class="brand__dot"></span>
      <span>Morrow Poolworks</span>
    </div>
    <p class="tagline">Clean Water. Safe Swims. Every Day.</p>
  </section>
</body>
</html>
```